Artificial Intelligence and Machine Learning Company Needs a New Website

We need a new web design for one of the leading companies in the Spanish market in the development of advanced analytics and artificial intelligence.
Our goal is to help in resolving complex planning decisions and improving the operational efficiency of our clients. We have big clients from different industries and very powerful technology partners. We want our new website to be clear and show our great experience in the sector (more than 10 years) and our young spirit.
Number of Pages Required
5+ page
Colors
Designer to choose colors to be used in the design.
Look and feel
Each slider illustrates characteristics of the customer's brand and the style your logo design should communicate.

```html
<!DOCTYPE html>
<html lang="en">
<head>
<meta charset="utf-8">
<title>clarion — planning, optimization, decision management</title>
<link rel="stylesheet" href="https://fonts.googleapis.com/css2?family=Mulish:ital,wght@0,400;0,600;0,700;1,600&display=swap">
<style>
:root{
  --orange:#fe5000;
  --ink:#222;
  --text:#333;
  --purple:#b33ad0;
  --grey:#e4e4e4;
  --line:#ddd;
  --white:#fff;
  --blue:#4a9fd8;
}
*{box-sizing:border-box;margin:0;padding:0}
html,body{width:1200px;height:3438px;overflow:hidden}
body{font-family:"Mulish",sans-serif;color:var(--text);background:var(--white);position:relative}
.wrap{width:732px;margin:0 auto;position:relative}
a{color:inherit;text-decoration:none}

/* header */
.site-header{height:60px;display:flex;align-items:center}
.site-header .wrap{display:flex;align-items:center}
.brand{font-size:29px;font-weight:700;color:var(--orange);display:flex;align-items:center;gap:8px;letter-spacing:-.5px}
.brand-dot{width:14px;height:14px;border-radius:50%;background:var(--purple)}
.main-nav{display:flex;gap:20px;margin-left:52px;font-size:9px;font-weight:600;color:var(--ink);white-space:nowrap}
.social{display:flex;gap:4px;margin-left:22px}
.social span{width:19px;height:19px;border-radius:50%;background:#111}
.lang{font-size:9px;color:#aaa;margin-left:24px}
.search{margin-left:30px}

/* hero */
.hero{height:413px;position:relative;background:linear-gradient(100deg,#3d3a37 0%,#6b5548 45%,#a77b5f 70%,#caa27a 100%)}
.hero-photo{position:absolute;inset:0}
.hero-copy{position:absolute;left:234px;top:130px;color:var(--white)}
.hero-copy h1{font-size:31px;font-weight:600;line-height:38px}
.hero-copy p{font-size:12px;font-weight:700;margin-top:12px}
.btn-outline{display:inline-block;margin-top:26px;border:2px solid var(--white);border-radius:20px;padding:8px 19px;font-size:12px;font-weight:600}

/* intro */
.intro{height:300px;display:flex;justify-content:space-between;width:732px;margin:0 auto;padding-top:56px}
.intro-col{width:290px;text-align:center;font-size:10px;line-height:16px;color:var(--ink)}
.intro-col h2{color:var(--orange);font-size:18px;font-weight:600;margin-bottom:12px}
.intro-icon{width:44px;height:40px;margin:0 auto 16px;background:linear-gradient(135deg,#d4e8f6,#9cc9ea)}
.intro-col p+p{margin-top:11px}

/* section titles */
.section-title{text-align:center;font-size:25px;font-weight:600;color:var(--ink)}
.section-title::after{content:"";display:block;width:150px;height:2px;background:var(--orange);margin:14px auto 0}

/* industries */
.industries{padding-top:2px;height:581px}
.industry-grid{display:grid;grid-template-columns:repeat(4,171px);gap:17px 16px;margin-top:40px}
.industry{height:202px;border:1px solid var(--line);text-align:center}
.industry .ph{height:131px}
.industry h3{height:70px;display:flex;align-items:center;justify-content:center;color:var(--orange);font-size:14px;font-weight:600;line-height:21px}

/* process */
.process{height:349px}
.timeline{position:relative;height:30px;margin-top:38px}
.timeline::before{content:"";position:absolute;left:0;right:0;top:12px;height:2px;background:var(--purple)}
.step-mark{position:absolute;top:7px;width:12px;height:12px;border-radius:50%;background:var(--orange)}
.steps{display:grid;grid-template-columns:repeat(4,170px);gap:17px;margin-top:18px}
.step h3{color:var(--orange);font-size:15px;font-weight:600}
.step .meta{font-size:10px;font-style:italic;font-weight:600;line-height:16px;margin-top:4px;color:var(--ink)}
.step p{font-size:8.5px;line-height:15px;margin-top:10px;text-align:justify;color:var(--ink)}

/* testimonial */
.testimonial{height:283px;background:var(--orange);color:var(--white);text-align:center;position:relative;padding-top:36px}
.testimonial blockquote{width:490px;margin:0 auto;font-size:12px;line-height:19px}
.testimonial .name{font-size:15px;font-weight:600;margin-top:26px;letter-spacing:.5px}
.testimonial .role{font-size:8px;margin-top:4px}
.btn-dark{display:inline-block;background:#111;border-radius:16px;padding:7px 20px;font-size:10px;font-weight:700;margin-top:16px}
.dots{display:flex;gap:5px;justify-content:center;margin-top:18px}
.dots span{width:6px;height:6px;border-radius:50%;background:#ff9a6d}
.dots span:first-child{background:var(--white)}
.arrow{position:absolute;top:132px}

/* technologies */
.technologies{height:525px;padding-top:67px}
.tech-grid{display:grid;grid-template-columns:repeat(6,116px);gap:8px;margin-top:58px;margin-left:1px}
.tech{height:308px;background:var(--grey);text-align:center;padding-top:20px}
.tech:nth-child(even){background:var(--white)}
.tech .icon{width:64px;height:64px;margin:0 auto 6px;border-radius:8px}
.tech h3{font-size:13px;font-weight:600;line-height:16px;color:var(--ink);height:48px;margin-top:6px}
.tech hr{border:0;border-top:1px solid #666;width:88px;margin:0 auto}
.tech p{font-size:8px;line-height:13.5px;padding:20px 12px 0;color:var(--ink);height:86px}
.learn{display:inline-block;background:var(--white);color:var(--orange);font-size:7px;padding:7px 15px;margin-top:10px;border:1px solid #f1f1f1}

/* clients */
.clients{height:130px;background:var(--orange);position:relative;display:flex;align-items:center;justify-content:center;gap:64px;color:var(--white)}
.client{font-size:17px;font-weight:700;display:flex;align-items:center;gap:7px}
.client i{display:block;width:14px;height:14px;background:var(--white)}
.client-arrow{position:absolute;top:63px;width:22px;height:22px;border-radius:50%;background:var(--white)}

/* contact */
.contact{height:552px;padding-top:70px}
.contact-options{display:flex;justify-content:center;gap:54px;margin-top:52px}
.option{display:flex;align-items:center;gap:24px;font-size:14px;line-height:21px;color:var(--ink)}
.option .ring{width:58px;height:58px;border-radius:50%;border:1.5px solid #f6a58a;display:flex;align-items:center;justify-content:center}
.building{width:650px;height:240px;margin:30px auto 0;background:linear-gradient(180deg,#fafafa,#eee);border-bottom:1px solid #aaa}

/* footer */
.site-footer{height:190px;background:var(--orange);color:var(--white);text-align:center;padding-top:63px;font-size:12px;font-weight:600;line-height:25px}
.site-footer div{display:flex;justify-content:center;align-items:center;gap:9px}
.bottom-bar{height:51px;display:flex;justify-content:space-between;align-items:center;width:732px;margin:0 auto;font-size:7.5px;color:var(--ink)}
</style>
</head>
<body>

<header class="site-header">
  <div class="wrap">
    <a class="brand" href="#">clarion<span class="brand-dot"></span></a>
    <nav class="main-nav">
      <a href="#">INDUSTRIES ˅</a><a href="#">TECHNOLOGIES ˅</a><a href="#">ABOUT US ˅</a><a href="#">RESOURCES</a><a href="#">PARTNERS</a>
    </nav>
    <div class="social"><span></span><span></span><span></span><span></span></div>
    <span class="lang">ES</span>
    <svg class="search" width="14" height="14" viewBox="0 0 14 14"><circle cx="8" cy="6" r="4.5" fill="none" stroke="#fe5000" stroke-width="1.5"/><path d="M5 9L1 13" stroke="#fe5000" stroke-width="1.5"/></svg>
  </div>
</header>

<section class="hero">
  <div class="hero-photo" role="img" aria-label="Photo of two colleagues chatting over coffee in a bright office"></div>
  <div class="hero-copy">
    <h1>planning, optimization,<br>decision management</h1>
    <p>Advanced Analytics and Artificial Intelligence for smart decisions</p>
    <a class="btn-outline" href="#">Interested to join us?</a>
  </div>
</section>

<section class="intro">
  <div class="intro-col">
    <h2>what we do</h2>
    <div class="intro-icon" role="img" aria-label="Icon of a branching process diagram"></div>
    <p>clarion4AI implements AI based solutions for supply chain planning &amp; optimization, workforce optimization and rule based decision management.</p>
  </div>
  <div class="intro-col">
    <h2>who we are</h2>
    <div class="intro-icon" role="img" aria-label="Icon of a computer monitor with a document"></div>
    <p>We consider ourselves the experts in mathematical optimization and rule based decision management. 15 years in business and many successful projects make that we can say this without the risk of disappointing you.</p>
    <p>We have carefully selected the world's best-in-class software suppliers as parners to work with.</p>
  </div>
</section>

<section class="industries wrap">
  <h2 class="section-title">areas &amp; industries</h2>
  <div class="industry-grid">
    <article class="industry"><div class="ph" role="img" aria-label="Photo of a technician working on an electrical panel" style="background:linear-gradient(160deg,#c9cdd3,#5a6a88)"></div><h3>field services</h3></article>
    <article class="industry"><div class="ph" role="img" aria-label="Photo of an insurance advisor meeting a couple" style="background:linear-gradient(160deg,#e3e5e8,#6a7d99)"></div><h3>insurance</h3></article>
    <article class="industry"><div class="ph" role="img" aria-label="Photo of a white truck on a highway" style="background:linear-gradient(160deg,#9eb4cf,#e2d6c6)"></div><h3>transportation &amp;<br>logistics</h3></article>
    <article class="industry"><div class="ph" role="img" aria-label="Photo of a team planning over a table" style="background:linear-gradient(160deg,#cfd7e0,#4b5c70)"></div><h3>workforce<br>planning</h3></article>
    <article class="industry"><div class="ph" role="img" aria-label="Photo of industrial silos against the sky" style="background:linear-gradient(180deg,#dce6ee,#5c6670)"></div><h3>manufacturing</h3></article>
    <article class="industry"><div class="ph" role="img" aria-label="Photo of an airliner engine at sunset" style="background:linear-gradient(160deg,#4f7fa8,#f2c99a)"></div><h3>aviation</h3></article>
    <article class="industry"><div class="ph" role="img" aria-label="Photo of a shopper with groceries" style="background:linear-gradient(160deg,#8a9a55,#d9c2a6)"></div><h3>retail</h3></article>
    <article class="industry"><div class="ph" role="img" aria-label="Photo of colleagues in a banking office" style="background:linear-gradient(160deg,#8a8f96,#cfc5b8)"></div><h3>banking</h3></article>
  </div>
</section>

<section class="process wrap">
  <h2 class="section-title">how we work</h2>
  <div class="timeline">
    <span class="step-mark" style="left:6px"></span>
    <span class="step-mark" style="left:193px"></span>
    <span class="step-mark" style="left:380px"></span>
    <span class="step-mark" style="left:567px"></span>
  </div>
  <div class="steps">
    <div class="step"><h3>Initial analysis</h3><div class="meta">Free of charge<br>0.5 - 1 day</div><p>Together we analyse the potential to improve your performance by applying smart planning. The result is a high level analysis including a clear explanation how you could increase performance. If there is no or little to win, we will you recommend not to invest any further.</p></div>
    <div class="step"><h3>Scan</h3><div class="meta">We only charge 50%<br>2 - 5 days</div><p>Our consultants conduct a scan to analyse your data and planning process. Objective is to determine in more detail the potential performance improvement and to define a high level project plan and investment.</p></div>
    <div class="step"><h3>Prototype</h3><div class="meta">We only charge 75%<br>5 - 15 days</div><p>Based on your data and resources, we build a prototype of a planning system that will give you real insight in the functioning of a solution. The prototype is the basis for further development in the project phase. Other deliverable is a detailed project plan.</p></div>
    <div class="step"><h3>Project</h3><p>Execution of the project. Development and implementation. First results. Learn more about the different engagement models below.</p></div>
  </div>
</section>

<section class="testimonial">
  <svg class="arrow" style="left:178px" width="12" height="20" viewBox="0 0 12 20"><path d="M10 2L2 10l8 8" fill="none" stroke="#fff" stroke-width="2"/></svg>
  <blockquote>“clarion has proven to be a reliable company with highly qualified technical staff who have been instrumental in upholding the commitments made. Thanks to the services it provided, incident resolution times have significantly dropped, which is why we consider it a great success.”</blockquote>
  <div class="name">MARTA RÍOS VIDAL</div>
  <div class="role">Head of the Operations Applications Department at GridCo</div>
  <a class="btn-dark" href="#">Success Stories</a>
  <div class="dots"><span></span><span></span><span></span></div>
  <svg class="arrow" style="left:1010px" width="12" height="20" viewBox="0 0 12 20"><path d="M2 2l8 8-8 8" fill="none" stroke="#fff" stroke-width="2"/></svg>
</section>

<section class="technologies wrap">
  <h2 class="section-title">technologies</h2>
  <div class="tech-grid">
    <article class="tech"><div class="icon" role="img" aria-label="Illustration for advanced analytics" style="background:linear-gradient(135deg,#9cc9ea,#4a9fd8)"></div><h3>advanced<br>analytics</h3><hr><p>Find out how we use predictive and prescriptive analytics to improve business performance.</p><a class="learn" href="#">LEARN HOW &nbsp;›</a></article>
    <article class="tech"><div class="icon" role="img" aria-label="Illustration for artificial intelligence" style="background:linear-gradient(135deg,#f2a0a0,#e84a4a)"></div><h3>artificial<br>intelligence</h3><hr><p>Find out how we use predictive and prescriptive analytics to improve business performance.</p><a class="learn" href="#">LEARN HOW &nbsp;›</a></article>
    <article class="tech"><div class="icon" role="img" aria-label="Illustration for rule-based systems" style="background:linear-gradient(135deg,#9cc9ea,#b33ad0)"></div><h3>rule-based<br>systems</h3><hr><p>Find out how we use predictive and prescriptive analytics to improve business performance.</p><a class="learn" href="#">LEARN HOW &nbsp;›</a></article>
    <article class="tech"><div class="icon" role="img" aria-label="Illustration for machine learning" style="background:linear-gradient(135deg,#7fc9c4,#e84a4a)"></div><h3>machine<br>learning</h3><hr><p>Find out how we use predictive and prescriptive analytics to improve business performance.</p><a class="learn" href="#">LEARN HOW &nbsp;›</a></article>
    <article class="tech"><div class="icon" role="img" aria-label="Illustration for mathematical optimization" style="background:linear-gradient(135deg,#f5c26b,#e84a4a)"></div><h3>mathematical<br>optimization</h3><hr><p>Find out how we use predictive and prescriptive analytics to improve business performance.</p><a class="learn" href="#">LEARN HOW &nbsp;›</a></article>
    <article class="tech"><div class="icon" role="img" aria-label="Illustration for flexible architecture" style="background:linear-gradient(135deg,#9cc9ea,#3aa6a0)"></div><h3>flexible<br>architecture</h3><hr><p>Find out how we use predictive and prescriptive analytics to improve business performance.</p><a class="learn" href="#">LEARN HOW &nbsp;›</a></article>
  </div>
</section>

<section class="clients" aria-label="Clients">
  <span class="client-arrow" style="left:186px"></span>
  <span class="client"><i></i>Norvale</span>
  <span class="client">Mercado</span>
  <span class="client">Transit</span>
  <span class="client">Aerona</span>
  <span class="client">Voltia</span>
  <span class="client-arrow" style="left:983px"></span>
</section>

<section class="contact">
  <h2 class="section-title">contact us</h2>
  <div class="contact-options">
    <div class="option"><span class="ring"><svg width="22" height="28" viewBox="0 0 22 28" fill="none" stroke="#f6a58a" stroke-width="1.4"><path d="M1 1h14l6 6v20H1zM15 1v6h6M5 13h12M5 17h12M5 21h12"/></svg></span><span>Information<br>request</span></div>
    <div class="option"><span class="ring"><svg width="30" height="24" viewBox="0 0 30 24" fill="none" stroke="#f6a58a" stroke-width="1.4"><rect x="1" y="1" width="28" height="18"/><circle cx="15" cy="10" r="5"/><path d="M15 10V6M10 23h10"/></svg></span><span>Ask for a<br>demo</span></div>
    <div class="option"><span class="ring"><svg width="28" height="28" viewBox="0 0 28 28" fill="none" stroke="#f6a58a" stroke-width="1.4"><path d="M4 16v-3a10 10 0 0 1 20 0v3"/><rect x="2" y="15" width="5" height="8" rx="2"/><rect x="21" y="15" width="5" height="8" rx="2"/><path d="M23 23c0 3-4 4-8 4"/></svg></span><span>Let us give<br>you a call</span></div>
  </div>
  <div class="building" role="img" aria-label="Line drawing of the office building facade"></div>
</section>

<footer class="site-footer">
  <div><svg width="12" height="16" viewBox="0 0 12 16"><path d="M6 0a6 6 0 0 1 6 6c0 4-6 10-6 10S0 10 0 6a6 6 0 0 1 6-6z" fill="#fff"/><circle cx="6" cy="6" r="2.2" fill="#fe5000"/></svg>C/Olmo, 22 4ª Planta 28010 Madrid (España)</div>
  <div><svg width="13" height="13" viewBox="0 0 13 13"><path d="M3 0l3 3-2 2c1 2 2 3 4 4l2-2 3 3-2 3C5 13 0 8 0 3z" fill="#fff"/></svg>+34 910 000 123</div>
  <div><svg width="15" height="11" viewBox="0 0 15 11"><rect width="15" height="11" fill="#fff"/><path d="M0 0l7.5 6L15 0" fill="none" stroke="#fe5000"/></svg>info@clarionsoluciones.es</div>
</footer>
<div class="bottom-bar">
  <span>Copyright © 2019 clarion. All Rights Reserved.</span>
  <span>Legal Notice &nbsp;|&nbsp; Cookies Policy &nbsp;|&nbsp; Privacy Policy</span>
</div>

</body>
</html>
```